"Steady Frame Slim Down Roadmap" eBook cover

THE TITLE HAS CHANGED SLIGHTLY TO ;
"Steady Frame Slim Down Roadmap"

The following is for a fat loss, health and fitness eBook titled "Steady Frame Slim Down Roadmap." This design should help promote and market this product, as well as intrigue those to not only make a purchase... but want to very much participate in the material and follow the material!

There is no restriction of color, idea, etc. PLEASE help me with your expertise in developing a great cover for this project...

THANKS SO MUCH

This book separates others just by the quality information provided. To much trial and error is wasted on false claims and overrated programs....I have provided the books topics below to hopefully give you a better understanding;
CHAPTER 1
Steady Frame Slimdown Manual
- What is it?
- Why it works?
- Why it will work for you?
CHAPTER 2
Kill Cardio
- Why cardio sucks?
- Myth about cardio?
- What cardio works for fat loss
CHAPTER 3
Iron vs. Machine
- What type of resistance training is best for fat loss?
- Why?
- The big pitfall to working on machines?
CHAPTER 4
Should You Really Eat That?
- Foods that build muscle
- Foods that burn fat
- Foods that suck!
CHAPTER 5
Playing With Iron
- Playing with iron
- 17 upper body builders
- 17 lower body builders
- 11 workouts in 11 minutes
CHAPTER 6
Buying Equipment On A Budget
- How to find dirt cheap dumbbells?
- How to build equipment under $100

THANKS AGAIN!

Target Market(s)

Self-Help / Health And Fitness / Nutrition

Industry/Entity Type

Health And Wellness

Font styles to use
Serif
Sans Serif
Other font styles liked:
• Tahoma, Verdana, Calibri

Requirements
Must have
• MUST MEET NORVEXA.example GUIDLINES ;
• File Types
• Lumira Author Hub currently accepts two types of files for cover images:
• JPEG (JPEG / JPG)
• TIFF (TIF / TIFF)
• We apply additional compression to images when displaying them on the website. For best results, please upload your images with minimal compression.
• Dimensions
• Requirements for the size of your cover art must have an ideal height/width ratio of at least 8:5 (1.6), meaning:
• • A minimum of 625 pixels on the shortest side and 1000 pixels on the longest side
• • For best quality, your image should be 2500 pixels on the longest side
• Important: We cannot accept any images larger than 10,000 pixels on the longest side.
• Size
• Your cover image must be less than 50MB. If the file type you are using supports compression, make sure to enable as little compression as possible, e.g. none for TIFF. Be sure to save your file with 72 dots per inch (DPI).
• Color
• Product images display on the Norvexa website using the RGB (red, green, blue) color mode or profile. RGB is the color mode native to the web and many color screen displays, as these three colors displayed at varying levels of intensity create over 16 million colors. When saving and uploading your cover image file, save your file ONLY as RGB - not CMYK or sRGB- for the color profile. You can usually find this option in the File saving dialog of image manipulation programs such as Photoshop.
• Some programs may also refer to RGB color as 'True Color' in some programs. If in doubt, try opening a JPG inside Internet Explorer, Firefox, or Safari. If a JPG opens fine inside a web browser, it's most likely okay to use as a cover image.
• Make sure to save your image without color separation. This is usually a pre-press or color palette option. Use your image manipulation program or image analysis tool (some are available free online) to verify that your image file doesn't have color separation.
• Use color images whenever possible and relevant. In addition to the Lumira black and white Z Slate reading devices, customers can read your books on full color Tessel devices and free Lumira reading apps for iPhone, iPad, Android, PC or Mac.
Should not have
• NO MALE OR FEMALE MODLES OR HALF NAKED PEOPLE...

```html
<!DOCTYPE html>
<html lang="en">
<head>
<meta charset="utf-8">
<title>Steady Frame Slim Down Roadmap — eBook Cover</title>
<link href="https://fonts.googleapis.com/css2?family=Cinzel:wght@400;700&family=Montserrat:wght@800&display=swap" rel="stylesheet">
<style>
  :root {
    --paper: #ffffff;
    --paper-shade: #e4e6e1;
    --title-blue: #1c4d9e;
    --title-teal: #17a19c;
    --teal-shadow: rgba(10, 70, 68, 0.35);
    --author-ink: #2a2a2a;
    --tape-yellow: #f3da3a;
    --tape-deep: #e2bd1e;
    --produce-red: #d8432c;
    --produce-orange: #f2a230;
    --produce-yellow: #efc93a;
    --produce-green: #5f8f34;
    --bottle-blue: #c9dceb;
    --steel: #9aa1a8;
    --table: #eef0ec;
  }
  html, body {
    margin: 0;
    padding: 0;
    width: 750px;
    height: 1200px;
    overflow: hidden;
    background: var(--paper);
  }
  .cover {
    position: relative;
    width: 750px;
    height: 1200px;
    overflow: hidden;
    background: radial-gradient(ellipse 80% 60% at 50% 40%, var(--paper) 0%, var(--paper) 50%, var(--paper-shade) 100%);
  }

  /* Measuring tape placeholder, top left */
  .tape-photo {
    position: absolute;
    left: 58px;
    top: -40px;
    width: 62px;
    height: 370px;
    border-radius: 10px;
    transform: rotate(-22deg);
    transform-origin: top center;
    background: linear-gradient(to bottom, var(--tape-yellow) 0%, var(--tape-deep) 100%);
    box-shadow: 3px 4px 8px rgba(0,0,0,0.15);
  }

  .author-name {
    position: absolute;
    top: 72px;
    left: 180px;
    width: 400px;
    margin: 0;
    text-align: center;
    font-family: "Cinzel", serif;
    font-weight: 400;
    font-size: 34px;
    line-height: 46px;
    letter-spacing: 3px;
    color: var(--author-ink);
  }

  .title {
    margin: 0;
    font-weight: normal;
  }
  .title-line {
    position: absolute;
    left: 0;
    width: 100%;
    text-align: center;
    white-space: nowrap;
  }
  .title-sans {
    font-family: "Montserrat", sans-serif;
    font-weight: 800;
    color: var(--title-blue);
  }
  .title-serif {
    font-family: "Cinzel", serif;
    font-weight: 700;
    color: var(--title-teal);
    text-shadow: 2px 3px 4px var(--teal-shadow);
  }
  .line-steady  { top: 262px; font-size: 74px;  line-height: 86px;  letter-spacing: 3px; padding-left: 10px; box-sizing: border-box; }
  .line-frame   { top: 350px; font-size: 160px; line-height: 170px; }
  .line-slim    { top: 548px; font-size: 104px; line-height: 124px; }
  .line-roadmap { top: 680px; font-size: 76px;  line-height: 90px;  letter-spacing: 7px; }

  /* Fruit, vegetables, water bottle and dumbbell placeholder */
  .produce-photo {
    position: absolute;
    left: 0;
    top: 800px;
    width: 750px;
    height: 400px;
    background:
      linear-gradient(to bottom, rgba(238,240,236,0) 0%, rgba(238,240,236,0) 80%, var(--table) 100%),
      linear-gradient(to right,
        var(--produce-red) 0%,
        var(--produce-orange) 16%,
        var(--produce-yellow) 26%,
        var(--produce-green) 40%,
        var(--produce-green) 50%,
        var(--produce-red) 64%,
        var(--bottle-blue) 78%,
        var(--steel) 92%,
        var(--steel) 100%);
    -webkit-mask-image: linear-gradient(to bottom, transparent 0%, rgba(0,0,0,0.6) 20%, #000 40%);
    mask-image: linear-gradient(to bottom, transparent 0%, rgba(0,0,0,0.6) 20%, #000 40%);
  }
</style>
</head>
<body>
  <main class="cover">
    <div class="tape-photo" role="img" aria-label="Yellow measuring tape curling down from the top left corner"></div>

    <p class="author-name">AUTHOR'S NAME</p>

    <h1 class="title">
      <span class="title-line title-sans line-steady">STEADY</span>
      <span class="title-line title-serif line-frame">FRAME</span>
      <span class="title-line title-serif line-slim">SLIM DOWN</span>
      <span class="title-line title-sans line-roadmap">ROADMAP</span>
    </h1>

    <div class="produce-photo" role="img" aria-label="Tomatoes, apple, yellow pepper, orange, broccoli and red pepper with a measuring tape, a water bottle and a chrome dumbbell on a white surface"></div>
  </main>
</body>
</html>
```